New Business Card Design

We would like to refresh our business cards and make them look better. We are an IT company specialising in Cloud Services, IT Managed Services, software and hardware. I have attached a PSD of our current design. Also attached our logo.
Updates

I have uploaded all new logos in EPS format.

Can you please edit all designs to include a job title for Marcus Hale, eg. General Manager

Industry/Entity Type

Software

Colors
ffffff

Requirements
Must have
• Please use white background.
Should not have
• Black background

```html
<!DOCTYPE html>
<html lang="en">
<head>
<meta charset="utf-8">
<title>Clarity Technology – Business Card</title>
<link href="https://fonts.googleapis.com/css2?family=Source+Sans+3:wght@400;600&display=swap" rel="stylesheet">
<style>
  :root {
    --bg: #e9e9ee;
    --card-white: #ffffff;
    --brand-red: #c0392b;
    --ink: #2b2b2e;
    --ink-soft: #4a4a4f;
    --rule: #b9b9be;
    --on-red: #ffffff;
  }
  * { margin: 0; padding: 0; box-sizing: border-box; }
  html, body { width: 1200px; height: 987px; overflow: hidden; }
  body {
    background: var(--bg);
    font-family: "Source Sans 3", "Helvetica Neue", Arial, sans-serif;
    color: var(--ink);
    position: relative;
  }
  .card {
    position: absolute;
    width: 540px;
    height: 330px;
    border-radius: 28px;
    box-shadow: 0 6px 18px rgba(0,0,0,0.12);
    overflow: hidden;
  }
  /* Front */
  .card-front { left: 50px; top: 329px; background: var(--card-white); }
  .brand {
    position: absolute; left: 40px; top: 40px;
    display: flex; align-items: center; gap: 14px;
  }
  .brand-dot { width: 40px; height: 40px; border-radius: 50%; background: var(--brand-red); }
  .brand-name {
    font-size: 34px; font-weight: 400; letter-spacing: 5px; color: var(--ink); line-height: 1;
  }
  .divider {
    position: absolute; left: 0; right: 0; top: 128px; height: 1px;
    background: linear-gradient(90deg, rgba(185,185,190,0) 0%, var(--rule) 30%, var(--rule) 85%, rgba(185,185,190,0.3) 100%);
  }
  .contact-list { position: absolute; left: 40px; top: 148px; list-style: none; }
  .contact-list li {
    display: flex; align-items: center; gap: 9px;
    font-size: 15px; line-height: 25px; color: var(--ink-soft);
  }
  .contact-list svg { width: 14px; height: 14px; fill: var(--brand-red); flex: none; }
  .holder { position: absolute; right: 40px; bottom: 34px; text-align: left; }
  .holder-name { font-size: 24px; font-weight: 600; color: var(--brand-red); line-height: 1.1; }
  .holder-title { font-size: 18px; color: var(--ink); }
  /* Back */
  .card-back { left: 610px; top: 329px; background: var(--brand-red); color: var(--on-red); }
  .back-mark {
    position: absolute; left: 50%; top: 46px; transform: translateX(-50%);
    display: flex; align-items: center; gap: 12px;
  }
  .back-mark-dot { width: 44px; height: 44px; border-radius: 50%; background: var(--on-red); }
  .back-mark-name { font-size: 36px; letter-spacing: 5px; font-weight: 400; }
  .back-copy {
    position: absolute; left: 0; right: 0; top: 168px; text-align: center;
    font-size: 19px; line-height: 1.35;
  }
  .back-url { margin-top: 10px; font-size: 14px; letter-spacing: 4px; }
</style>
</head>
<body>
  <section class="card card-front">
    <div class="brand">
      <span class="brand-dot"></span>
      <span class="brand-name">clarity technology</span>
    </div>
    <div class="divider"></div>
    <ul class="contact-list">
      <li><svg viewBox="0 0 16 16"><path d="M3.5 1.5l2.5 0 1 3.5-1.8 1.2a9 9 0 0 0 4.6 4.6L11 9l3.5 1v2.5c0 1-1 2-2 2C6.5 14.5 1.5 9.5 1.5 3.5c0-1 1-2 2-2z"/></svg>07 3555 0142</li>
      <li><svg viewBox="0 0 16 16"><path d="M4.5 0.5h7a1 1 0 0 1 1 1v13a1 1 0 0 1-1 1h-7a1 1 0 0 1-1-1v-13a1 1 0 0 1 1-1zm0.8 2v9h5.4v-9zM8 12.5a1 1 0 1 0 0 2 1 1 0 0 0 0-2z"/></svg>0400 555 218</li>
      <li><svg viewBox="0 0 16 16"><path d="M1 3.5h14v9H1zm1.3 1.2L8 9l5.7-4.3z"/></svg>mhale@claritynet.com.au</li>
      <li><svg viewBox="0 0 16 16"><path d="M8 1a7 7 0 1 0 0 14A7 7 0 0 0 8 1zm-0.7 1.6v2.6H5.1c.5-1.4 1.3-2.4 2.2-2.6zm1.4 0c.9.2 1.7 1.2 2.2 2.6H8.7zM4.7 6.5h2.6v2.9H4.6a9 9 0 0 1 .1-2.9zm4 0h2.6a9 9 0 0 1 .1 2.9H8.7zm-1.4 4.2v2.7c-.9-.2-1.7-1.2-2.2-2.7zm1.4 0h2.2c-.5 1.5-1.3 2.5-2.2 2.7z"/></svg>www.claritynet.com.au</li>
    </ul>
    <div class="holder">
      <p class="holder-name">Marcus Hale</p>
      <p class="holder-title">General Manager</p>
    </div>
  </section>

  <section class="card card-back">
    <div class="back-mark">
      <span class="back-mark-dot"></span>
      <span class="back-mark-name">clarity</span>
    </div>
    <div class="back-copy">
      <p>We are an IT company specializing in Cloud Services</p>
      <p>IT Managed Services, software and hardware</p>
      <p class="back-url">www.claritynet.com.au</p>
    </div>
  </section>
</body>
</html>
```